401K Retirement Plan Consultant

Professional & clean lines - not overly busy. We offer two services - 401k administration and HSA administration. Based on the outskirts of Charlotte NC. Communicate the services we offer along with the financial institutions that we work with. Mixture of icons and people pictures.

Current website - tvh401k.com,
It is presently very amateurish.

```html
<!DOCTYPE html>
<html lang="en">
<head>
<meta charset="utf-8">
<title>TVH401k – Employee Benefits</title>
<link href="https://fonts.googleapis.com/css2?family=Bebas+Neue&family=Roboto:wght@400;500;700&display=swap" rel="stylesheet">
<style>
:root{
  --blue:#0707d9;
  --green:#4caf50;
  --ink:#111111;
  --text:#222222;
  --muted:#f5f5f5;
  --line:#d8d8d8;
  --white:#ffffff;
}
*{box-sizing:border-box;margin:0;padding:0}
html,body{width:1200px;height:3013px;overflow:hidden;background:var(--white)}
body{position:relative;font-family:'Roboto',sans-serif;color:var(--text)}
.abs{position:absolute}
.brand{font-family:'Roboto',sans-serif;font-weight:700;color:var(--ink);letter-spacing:.5px}
.btn{position:absolute;display:flex;align-items:center;justify-content:center;background:var(--blue);color:var(--white);font-size:13px;font-weight:700;border-radius:18px;text-decoration:none}
.nav-link{position:absolute;top:24px;font-size:13px;color:var(--ink)}
.header-btn{border-radius:0;font-weight:400;font-size:13px}
.hero-photo{left:0;top:63px;width:1200px;height:530px;background:linear-gradient(90deg,#8a6a3a 0%,#c99850 30%,#f2c97a 55%,#fbe7b8 75%,#fff5e2 100%)}
.hero-fade{left:560px;top:63px;width:640px;height:483px;background:linear-gradient(180deg,rgba(255,255,255,.9) 0%,rgba(255,250,240,.6) 60%,rgba(240,190,90,.5) 100%)}
.hero-title{left:660px;top:190px;width:480px;font-family:'Bebas Neue',sans-serif;font-weight:400;font-size:58px;line-height:57px;color:var(--ink);white-space:nowrap}
.partner-bar{left:141px;top:546px;width:1059px;height:95px;background:var(--white);border:1px solid #e6e6e6}
.partner-name{position:absolute;top:36px;font-size:17px;font-weight:500;color:#333;white-space:nowrap}
.section-title{position:absolute;font-size:34px;font-weight:500;color:var(--ink)}
.about-photo{left:141px;top:752px;width:453px;height:337px;border-radius:4px;background:linear-gradient(135deg,#e4e8ee 0%,#9aa6b6 45%,#5a7aa6 100%)}
.body-text{position:absolute;font-size:12.5px;line-height:22.7px;color:var(--text)}
.check-item{position:absolute;display:flex;align-items:center;gap:14px;font-size:12.5px;color:var(--text);white-space:nowrap}
.check-item svg{width:17px;height:17px}
.service-label{position:absolute;font-size:17px;font-weight:500;line-height:23px;color:var(--ink)}
.band{left:0;top:1925px;width:1200px;height:463px;background:var(--muted)}
.other-photo{left:606px;top:2010px;width:452px;height:293px;border-radius:4px;background:linear-gradient(120deg,#b9c9a9 0%,#e9e3d6 40%,#d8b59a 70%,#c07a4a 100%)}
.card{position:absolute;top:2533px;width:141px;height:74px;background:var(--white);box-shadow:0 2px 8px rgba(0,0,0,.06);display:flex;align-items:center;justify-content:center;font-size:14px;font-weight:500;color:#333;white-space:nowrap}
.footer{left:0;top:2694px;width:1200px;height:284px;background:var(--muted)}
.foot-head{position:absolute;top:2756px;font-size:14px;font-weight:700;color:var(--ink)}
.foot-link{position:absolute;left:141px;font-size:12.5px;color:var(--ink)}
.foot-icon{position:absolute;width:32px;height:32px;border-radius:50%;background:var(--blue);display:flex;align-items:center;justify-content:center}
.foot-icon svg{width:16px;height:16px}
.foot-text{position:absolute;font-size:12.5px;line-height:15px;color:var(--ink);white-space:nowrap}
.foot-text b{font-weight:500}
.copyright{left:0;top:2978px;width:1200px;height:35px;background:var(--blue);color:var(--white);font-size:12.5px;font-weight:500;display:flex;align-items:center;justify-content:center}
</style>
</head>
<body>
<svg width="0" height="0" style="position:absolute">
  <defs>
    <symbol id="tick" viewBox="0 0 20 20"><circle cx="10" cy="10" r="8.5" fill="none" stroke="#222" stroke-width="1.3"/><path d="M6.3 10.3l2.6 2.6 4.9-5.2" fill="none" stroke="#222" stroke-width="1.3"/></symbol>
    <symbol id="tick-blue" viewBox="0 0 20 20"><circle cx="10" cy="10" r="8.5" fill="none" stroke="#0707d9" stroke-width="1.3"/><path d="M6.3 10.3l2.6 2.6 4.9-5.2" fill="none" stroke="#0707d9" stroke-width="1.3"/></symbol>
  </defs>
</svg>

<!-- Header -->
<header>
  <div class="abs brand" style="left:141px;top:14px;font-size:26px">TVH401k</div>
  <span class="nav-link" style="left:785px">Home</span>
  <span class="nav-link" style="left:861px">About Us</span>
  <a class="btn header-btn" style="left:957px;top:14px;width:101px;height:35px">Contact Us</a>
</header>

<!-- Hero -->
<section>
  <div class="abs hero-photo" role="img" aria-label="Family of three outdoors at sunset, child on father's shoulders holding a national flag"></div>
  <div class="abs hero-fade"></div>
  <h1 class="abs hero-title">TVH401k has been<br>providing employee<br>benefits services<br>since 1987</h1>
  <div class="abs partner-bar">
    <span class="partner-name" style="left:29px">Faxton Trust</span>
    <span class="partner-name" style="left:189px">Alvora</span>
    <span class="partner-name" style="left:352px">Emberline</span>
    <span class="partner-name" style="left:492px">Quellford Funds</span>
    <span class="partner-name" style="left:636px">Vantra</span>
    <span class="partner-name" style="left:787px">Waltham Kline</span>
  </div>
</section>

<!-- About -->
<section>
  <div class="abs about-photo" role="img" aria-label="Two businessmen shaking hands in a bright office"></div>
  <h2 class="section-title" style="left:651px;top:752px">About TVH401k</h2>
  <p class="body-text" style="left:651px;top:795px;width:410px">TVH has been providing employee benefit services since 1987.&nbsp;&nbsp; Our plans gives you the flexibility to customize a retirement plan that meets the specific needs of your company and the employees. Our IRS approved 401(k) plans are:</p>
  <div class="check-item" style="left:651px;top:896px"><svg><use href="#tick"/></svg>Designed Especially For Smaller Plans</div>
  <div class="check-item" style="left:651px;top:927px"><svg><use href="#tick"/></svg>Simple To Operate And Maintain</div>
  <div class="check-item" style="left:651px;top:958px"><svg><use href="#tick"/></svg>Low-Cost Recordkeeping And Investments</div>
  <p class="body-text" style="left:651px;top:985px;width:410px">Contact us today to request a custom fee comparison or a quote for a startup plan.&nbsp; It's quick and easy.</p>
  <a class="btn" style="left:651px;top:1048px;width:106px;height:34px">Contact Us</a>
</section>

<!-- Services -->
<section>
  <h2 class="section-title" style="left:0;width:1200px;text-align:center;top:1167px">Our Services</h2>
  <svg class="abs" style="left:0;top:1270px" width="1200" height="480" viewBox="0 0 1200 480">
    <circle cx="585" cy="245" r="208" fill="none" stroke="#bdbdbd" stroke-width="1"/>
    <circle cx="585" cy="245" r="128" fill="#f4f4f4" stroke="#111" stroke-width="4"/>
    <g fill="#0707d9">
      <circle cx="589" cy="33" r="34"/><circle cx="458" cy="86" r="34"/><circle cx="788" cy="222" r="34"/><circle cx="407" cy="345" r="34"/><circle cx="654" cy="432" r="34"/>
    </g>
    <g fill="#4caf50">
      <circle cx="727" cy="95" r="34"/><circle cx="386" cy="214" r="34"/><circle cx="761" cy="346" r="34"/><circle cx="510" cy="429" r="34"/>
    </g>
    <g fill="none" stroke="#fff" stroke-width="1.6">
      <rect x="578" y="20" width="22" height="26" rx="2"/><circle cx="589" cy="33" r="5"/>
      <path d="M446 98h24M448 98v-12h20v12M444 86l14-9 14 9"/>
      <circle cx="727" cy="90" r="5"/><circle cx="717" cy="96" r="4"/><circle cx="737" cy="96" r="4"/><path d="M723 106h8"/>
      <circle cx="389" cy="208" r="8"/><path d="M374 224h10l6-4h8"/>
      <circle cx="788" cy="212" r="5"/><circle cx="780" cy="230" r="5"/><circle cx="796" cy="230" r="5"/>
      <circle cx="407" cy="343" r="10"/><path d="M403 343h8M407 339v8"/>
      <rect x="749" y="334" width="24" height="14"/><path d="M751 356h20"/>
      <circle cx="510" cy="429" r="12"/><circle cx="510" cy="425" r="3"/>
      <rect x="641" y="421" width="26" height="20"/><path d="M645 427h8M645 433h8M657 427h6"/>
    </g>
  </svg>
  <div class="abs brand" style="left:485px;top:1495px;width:200px;text-align:center;font-size:36px">TVH401k</div>

  <div class="service-label" style="left:389px;width:400px;text-align:center;top:1233px">Open Architecture Platform</div>
  <div class="service-label" style="left:109px;width:300px;text-align:right;top:1338px">COBRA Administration</div>
  <div class="service-label" style="left:778px;top:1338px">IRS 5500 &amp; 1099-R's</div>
  <div class="service-label" style="left:136px;width:200px;text-align:right;top:1465px">FSA, HRA and<br>Dependent Care</div>
  <div class="service-label" style="left:837px;top:1470px">Employer Allocation<br>Preparation</div>
  <div class="service-label" style="left:107px;width:250px;text-align:right;top:1614px">HSA Administration</div>
  <div class="service-label" style="left:812px;top:1621px">Employee Education</div>
  <div class="service-label" style="left:249px;width:400px;text-align:center;top:1747px">Non-Discrimination Testing</div>
  <div class="service-label" style="left:560px;width:400px;text-align:center;top:1750px">Plan Design &amp; Document Services</div>
  <a class="btn" style="left:547px;top:1806px;width:106px;height:35px">Contact Us</a>
</section>

<!-- Other services -->
<section>
  <div class="abs band"></div>
  <h2 class="section-title" style="left:141px;top:2027px">Other Services</h2>
  <div class="check-item" style="left:141px;top:2081px"><svg><use href="#tick"/></svg>Health Saving Account</div>
  <div class="check-item" style="left:141px;top:2112px"><svg><use href="#tick"/></svg>Flexible Spending Account</div>
  <div class="check-item" style="left:141px;top:2143px"><svg><use href="#tick"/></svg>Health Reimbursement Account</div>
  <div class="check-item" style="left:141px;top:2174px;color:var(--blue);font-weight:500"><svg><use href="#tick-blue"/></svg>Health Insurance Continuation</div>
  <div class="check-item" style="left:141px;top:2205px"><svg><use href="#tick"/></svg>Dependent Care</div>
  <a class="btn" style="left:141px;top:2244px;width:106px;height:34px">Contact Us</a>
  <div class="abs other-photo" role="img" aria-label="Smiling senior couple reviewing a plan on a clipboard with an adviser"></div>
</section>

<!-- Partners -->
<section>
  <h2 class="section-title" style="left:0;width:1200px;text-align:center;top:2465px">Our Partners</h2>
  <svg class="abs" style="left:104px;top:2559px" width="22" height="22" viewBox="0 0 22 22"><circle cx="11" cy="11" r="10" fill="none" stroke="#111" stroke-width="1.5"/><path d="M13 6l-5 5 5 5" fill="none" stroke="#111" stroke-width="1.5"/></svg>
  <div class="card" style="left:141px">Faxton Trust</div>
  <div class="card" style="left:297px">Quellford Funds</div>
  <div class="card" style="left:451px">Vantra</div>
  <div class="card" style="left:607px">Emberline</div>
  <div class="card" style="left:761px">Alvora</div>
  <div class="card" style="left:918px">Waltham Kline</div>
  <svg class="abs" style="left:1073px;top:2559px" width="22" height="22" viewBox="0 0 22 22"><circle cx="11" cy="11" r="10" fill="none" stroke="#111" stroke-width="1.5"/><path d="M9 6l5 5-5 5" fill="none" stroke="#111" stroke-width="1.5"/></svg>
</section>

<!-- Footer -->
<footer>
  <div class="abs footer"></div>
  <div class="foot-head" style="left:141px">Quick Links</div>
  <span class="foot-link" style="top:2786px">Home</span>
  <span class="foot-link" style="top:2813px">About Us</span>
  <span class="foot-link" style="top:2840px">Contact Us</span>

  <div class="foot-head" style="left:323px">Contact Details</div>
  <div class="foot-icon" style="left:322px;top:2787px"><svg viewBox="0 0 16 16"><path d="M8 1.5a4.5 4.5 0 0 0-4.5 4.5c0 3.4 4.5 8.5 4.5 8.5s4.5-5.1 4.5-8.5A4.5 4.5 0 0 0 8 1.5z" fill="none" stroke="#fff" stroke-width="1.2"/><circle cx="8" cy="6" r="1.6" fill="none" stroke="#fff" stroke-width="1.2"/></svg></div>
  <div class="foot-text" style="left:368px;top:2788px">2180 Lakeshore Pkwy Suite 105<br>Harbor Point SC 29700</div>
  <div class="foot-icon" style="left:322px;top:2838px"><svg viewBox="0 0 16 16"><path d="M4 2l2.5 3-1.5 1.5c.8 1.8 2.2 3.2 4 4l1.5-1.5 3 2.5-1.5 2C7 13 3 9 2 3.5z" fill="none" stroke="#fff" stroke-width="1.2"/></svg></div>
  <div class="foot-text" style="left:368px;top:2840px"><b>Call Us</b><br>1 704 555 0142</div>
  <div class="foot-icon" style="left:322px;top:2889px"><svg viewBox="0 0 16 16"><rect x="2" y="4" width="12" height="8" fill="none" stroke="#fff" stroke-width="1.2"/><path d="M2 4l6 5 6-5" fill="none" stroke="#fff" stroke-width="1.2"/></svg></div>
  <div class="foot-text" style="left:368px;top:2891px"><b>Email Us</b><br>service@tvh401k.com</div>

  <div class="foot-head" style="left:641px">Follow Us</div>
  <div class="foot-icon" style="left:641px;top:2787px"></div>
  <div class="foot-text" style="left:689px;top:2796px">Friendbook</div>
  <div class="foot-icon" style="left:641px;top:2839px"></div>
  <div class="foot-text" style="left:689px;top:2848px">Pictagram</div>
  <div class="foot-icon" style="left:641px;top:2892px"></div>
  <div class="foot-text" style="left:689px;top:2901px">Linkwork</div>

  <div class="abs brand" style="left:830px;top:2765px;font-size:36px">TVH401k</div>
  <p class="body-text" style="left:834px;top:2832px;width:230px;font-size:11.5px">TVH's retirement plan solutions are designed to serve a broad range of clients and offer the advantages of large-plan pricing to small employer-sponsored retirement plans.</p>
  <div class="abs copyright">© 2024 TVH401k. All Rights Reserved</div>
</footer>
</body>
</html>
```